Varoden Imports Busisness cards and logo

Varoden imports is a brand new wholesale company located in Londonderry, New Hampshire dedicated to finding unique products from around the world.
Licensed to sell wine and spirits in the state and also authorized distributors of Blue Pepper Design, a manufacturer of girls and women shoes. Other products that we are currently trying to import are cheese and frozen food from Spain.
We would like a design that portraits our diversity of products and wholesale capabilities
Updates

Industry/Entity Type

It Company

```html
<!DOCTYPE html>
<html lang="en">
<head>
<meta charset="utf-8">
<title>Varoden Imports – Business Card</title>
<link href="https://fonts.googleapis.com/css2?family=Open+Sans:wght@400;600;700;800&display=swap" rel="stylesheet">
<style>
  :root {
    --page-bg: #f2f4f7;
    --card-sky-light: #cfeefc;
    --card-sky: #8fd4f5;
    --card-sky-deep: #3fa9e6;
    --ink-navy: #1f3a8f;
    --accent-red: #e4262b;
    --globe-deep: #1d3f9e;
    --globe-mid: #3a6cc9;
    --globe-light: #7fa9e6;
  }
  html, body {
    margin: 0;
    width: 1200px;
    height: 900px;
    overflow: hidden;
    background: var(--page-bg);
    font-family: "Open Sans", sans-serif;
  }
  .business-card {
    position: absolute;
    left: 100px;
    top: 164px;
    width: 1000px;
    height: 572px;
    border-radius: 40px;
    overflow: hidden;
    background: linear-gradient(120deg, var(--card-sky-light) 0%, var(--card-sky) 45%, var(--card-sky-deep) 100%);
    box-shadow: 0 10px 30px rgba(0, 0, 0, 0.12);
  }
  .world-network-art {
    position: absolute;
    inset: 0;
    background:
      radial-gradient(ellipse at 60% 55%, rgba(255, 255, 255, 0.55) 0%, rgba(255, 255, 255, 0) 45%),
      linear-gradient(160deg, rgba(255, 255, 255, 0.35) 0%, rgba(255, 255, 255, 0) 60%);
  }
  .globe-cargo-art {
    position: absolute;
    left: 690px;
    top: 210px;
    width: 420px;
    height: 420px;
    border-radius: 50%;
    background: radial-gradient(circle at 40% 35%, var(--globe-light) 0%, var(--globe-mid) 40%, var(--globe-deep) 80%);
  }
  .brand-name {
    position: absolute;
    left: 62px;
    top: 50px;
    margin: 0;
    font-size: 72px;
    font-weight: 800;
    letter-spacing: 2px;
    color: var(--ink-navy);
    text-transform: uppercase;
    line-height: 1;
    white-space: nowrap;
  }
  .person {
    position: absolute;
    left: 62px;
    top: 228px;
  }
  .person-name {
    margin: 0;
    font-size: 38px;
    font-weight: 700;
    color: var(--accent-red);
    line-height: 1.1;
  }
  .person-title {
    margin: 2px 0 0;
    font-size: 22px;
    font-weight: 400;
    color: var(--ink-navy);
  }
  .contact-list {
    position: absolute;
    left: 62px;
    top: 342px;
    margin: 0;
    padding: 0;
    list-style: none;
    font-size: 26px;
    font-weight: 600;
    color: var(--ink-navy);
    line-height: 38px;
  }
  .contact-item {
    display: flex;
    align-items: flex-start;
  }
  .contact-icon {
    width: 26px;
    height: 26px;
    margin: 6px 10px 0 0;
    flex: none;
    fill: var(--accent-red);
  }
</style>
</head>
<body>
  <article class="business-card">
    <div class="world-network-art" role="img" aria-label="World map with network grid lines"></div>
    <div class="globe-cargo-art" role="img" aria-label="Globe surrounded by shipping boxes"></div>

    <h1 class="brand-name">Varoden Imports</h1>

    <div class="person">
      <p class="person-name">MATEO R.ALVAR</p>
      <p class="person-title">V.P of Sale</p>
    </div>

    <ul class="contact-list">
      <li class="contact-item">
        <svg class="contact-icon" viewBox="0 0 24 24" aria-hidden="true"><path d="M6.6 10.8a15.1 15.1 0 0 0 6.6 6.6l2.2-2.2c.3-.3.7-.4 1-.2 1.1.4 2.3.6 3.6.6.6 0 1 .4 1 1V20c0 .6-.4 1-1 1C10.6 21 3 13.4 3 4c0-.6.4-1 1-1h3.5c.6 0 1 .4 1 1 0 1.3.2 2.5.6 3.6.1.3 0 .7-.2 1z"/></svg>
        <span>603-555-0147</span>
      </li>
      <li class="contact-item">
        <svg class="contact-icon" viewBox="0 0 24 24" aria-hidden="true"><path d="M3 6h18v12H3z M3 6l9 7 9-7" fill="none" stroke="var(--accent-red)" stroke-width="2.4"/></svg>
        <span>malvar2007@northmail.net</span>
      </li>
      <li class="contact-item">
        <svg class="contact-icon" viewBox="0 0 24 24" aria-hidden="true"><path d="M12 3 2 12h3v9h5v-6h4v6h5v-9h3z"/></svg>
        <span>P.O.Box 418<br>Marlow Ridge, ME 04127-0418<br>USA</span>
      </li>
    </ul>
  </article>
</body>
</html>
```